New web design for a service provider in the medical field

We are looking for a new design for our website. We are a company that repairs and sells medical endoscopes. Our customers include doctors and hospitals. Our current website can be found at https://lumenfix.example/en/lumenfix-english.
We need a new web design (without programming) for the following 3 pages:
-Startpage https://lumenfix.example/en/lumenfix-english/
-Used endoscopes https://lumenfix.example/en/used-endoscopes/
-Purchase https://lumenfix.example/en/purchase/
The design should be modern and stylish.
The blue color of the logo should be reflected on the page, but not too intrusive.
I have uploaded the images from the header. If more images are needed, let me know and I will upload them.

Target Market(s)
Doctors and hospitals

```html
<!DOCTYPE html>
<html lang="en">
<head>
<meta charset="utf-8">
<title>LumenFix – Endoscope Repair and Sale</title>
<link rel="stylesheet" href="https://fonts.googleapis.com/css2?family=Poppins:wght@400;500;600;700&family=Roboto:wght@400;500;700;900&display=swap">
<style>
:root{
  --blue:#0a5cc2;
  --blue-dark:#063f93;
  --blue-deep:#02307a;
  --blue-light:#7fb3e6;
  --ink:#111;
  --text:#555;
  --muted:#6b6b6b;
  --white:#fff;
  --black:#000;
}
*{margin:0;padding:0;box-sizing:border-box}
html,body{width:1200px;height:3500px;overflow:hidden}
body{position:relative;font-family:'Poppins',sans-serif;color:var(--ink);background:var(--white)}
.abs{position:absolute}
a{color:inherit;text-decoration:none}

/* header */
.topbar{left:510px;top:0;width:690px;height:37px;background:var(--blue);clip-path:polygon(0 0,100% 0,100% 100%,14px 100%);border-bottom-left-radius:14px;color:var(--white);font-size:10px;display:flex;align-items:center;gap:0;padding-left:44px}
.topbar .item{display:flex;align-items:center;gap:8px}
.topbar .sep{width:1px;height:14px;background:var(--white);margin:0 14px}
.topbar .search{display:flex;justify-content:space-between;align-items:center;width:132px;border-bottom:1px solid var(--white);padding-bottom:2px}
.brand{left:95px;top:22px;display:flex;align-items:center;gap:8px;font-family:'Poppins',sans-serif;font-weight:600;font-size:20px;color:var(--blue-dark)}
.brand .dot{width:14px;height:14px;border-radius:50%;background:var(--blue)}
.nav{top:54px;left:431px;display:flex;gap:27px;font-size:11.5px;font-weight:600;color:var(--ink)}

/* hero */
.hero{left:0;top:88px;width:1200px;height:714px;background:radial-gradient(ellipse at 35% 35%,#4aa3ff 0%,#1565e0 40%,#0848b8 75%,#053a9a 100%)}
.hero-title{left:0;top:332px;width:1200px;text-align:center;font-family:'Roboto',sans-serif;font-weight:900;font-size:46px;color:var(--white);letter-spacing:.3px;text-shadow:0 2px 6px rgba(0,0,0,.25)}
.hero-text{left:140px;top:400px;width:920px;text-align:center;font-size:18px;line-height:30px;color:var(--white)}
.btn{display:flex;align-items:center;justify-content:center;border-radius:30px;font-family:'Roboto',sans-serif;font-weight:700;text-transform:uppercase}
.hero-btn{top:489px;width:207px;height:44px;font-size:17px}
.btn-white{background:var(--white);color:var(--blue)}
.btn-dark{background:var(--blue-dark);color:var(--white);box-shadow:0 3px 8px rgba(0,0,0,.25)}
.arrow-circle{width:30px;height:30px;border:2px solid var(--white);border-radius:50%;display:flex;align-items:center;justify-content:center}
.dots{left:584px;top:727px;display:flex;gap:4px}
.dots span{width:8px;height:8px;border-radius:50%;background:var(--white)}

/* section headings */
.h2{font-family:'Roboto',sans-serif;font-weight:700;font-size:30px;text-transform:uppercase;color:var(--ink)}
.center{text-align:center;left:0;width:1200px}
.sub{font-size:15px;color:var(--text)}
.copy{font-size:13.5px;line-height:22.5px;color:var(--text)}

/* about */
.btn-blue{background:var(--blue-dark);color:var(--white)}
.about-photo{left:618px;top:874px;width:452px;height:375px;border-radius:30px;background:linear-gradient(135deg,#d9dde2,#9fa7b1 55%,#e9edf1)}
.about-accent{left:840px;top:1080px;width:265px;height:202px;background:var(--blue-dark);border-radius:14px;clip-path:polygon(88% 0,100% 0,100% 100%,0 100%,0 88%)}

/* services */
.svc{width:340px;text-align:center}
.svc-card{left:427px;top:1477px;width:338px;height:388px;background:var(--white);border-radius:16px;box-shadow:0 4px 18px rgba(0,0,0,.16)}
.icon-circle{width:90px;height:90px;border-radius:50%;background:#dbe8f7;margin:0 auto;display:flex;align-items:center;justify-content:center}
.svc h3{font-family:'Roboto',sans-serif;font-weight:500;font-size:23px;margin-top:16px}
.svc h4{font-family:'Roboto',sans-serif;font-weight:400;font-size:19px;color:var(--muted);margin-top:8px}
.svc p{font-size:13.5px;line-height:22px;color:var(--muted);margin:14px auto 0;width:260px;height:66px;overflow:hidden}
.svc .btn{width:225px;height:40px;font-size:15px;margin:18px auto 0;background:var(--blue-dark);color:var(--white)}

/* outcome */
.feat{width:253px;height:316px;background:var(--white);border-radius:22px;text-align:center;padding-top:52px;box-shadow:0 4px 14px rgba(0,0,0,.1)}
.feat .pin{position:absolute;left:118px;top:40px;width:16px;height:16px;border-radius:50%;border:2px solid var(--blue);background:var(--white);z-index:2}
.feat .ic{width:90px;height:90px;border-radius:50%;background:var(--blue);margin:0 auto;display:flex;align-items:center;justify-content:center}
.feat h3{font-family:'Roboto',sans-serif;font-weight:700;font-size:17px;color:var(--blue);text-transform:uppercase;margin:22px 20px 0;line-height:21px}
.feat p{font-size:13px;line-height:21px;color:#222;margin:10px 24px 0}

/* used */
.prod{width:293px;height:361px;background:var(--white);box-shadow:0 3px 12px rgba(0,0,0,.14)}
.prod .ph{height:191px}
.prod h3{font-size:15px;font-weight:600;line-height:20px;margin:20px 12px 0}
.prod p{font-size:13.5px;line-height:20px;color:var(--muted);margin:6px 14px 0}
.prod .more{font-size:13.5px;font-weight:700;color:var(--blue);margin:8px 14px 0;display:block}
.small-arrow{width:24px;height:24px;border:1px solid #888;border-radius:50%;display:flex;align-items:center;justify-content:center}

/* cta / footer */
.footer-bg{left:0;top:3051px;width:1200px;height:449px;background:var(--black)}
.cta{left:94px;top:3014px;width:1011px;height:186px;border-radius:93px;background:linear-gradient(90deg,#0a66cc,#0f8ee0 60%,#0a72d4)}
.cta h2{position:absolute;left:79px;top:50px;font-family:'Roboto',sans-serif;font-weight:700;font-size:29px;line-height:34px;color:var(--white);text-transform:uppercase}
.cta .btn{position:absolute;left:762px;top:71px;width:172px;height:42px;background:var(--white);color:var(--blue);font-size:16px}
.f-head{font-family:'Roboto',sans-serif;font-weight:700;font-size:16px;color:var(--white);text-transform:uppercase}
.f-links{list-style:none;font-size:12px;color:var(--white);line-height:24.5px}
.f-text{font-size:12px;line-height:21px;color:var(--white)}
.subscribe{left:881px;top:3311px;width:224px;height:34px;border:1px solid var(--white);border-radius:20px;background:var(--white);display:flex;align-items:center;font-size:11.5px;color:#333;padding-left:18px}
.subscribe .send{position:absolute;right:0;top:0;height:32px;width:104px;background:var(--blue);color:var(--white);border-radius:20px;font-weight:700;display:flex;align-items:center;justify-content:center}
</style>
</head>
<body>

<!-- header -->
<div class="abs brand"><span class="dot"></span>LumenFix</div>
<div class="abs topbar">
  <div class="item">
    <svg width="12" height="12" viewBox="0 0 24 24"><path fill="#fff" d="M6.6 10.8a15.1 15.1 0 0 0 6.6 6.6l2.2-2.2c.3-.3.7-.4 1-.2 1.1.4 2.3.6 3.6.6.6 0 1 .4 1 1V20c0 .6-.4 1-1 1A17 17 0 0 1 3 4c0-.6.4-1 1-1h3.5c.6 0 1 .4 1 1 0 1.3.2 2.5.6 3.6.1.3 0 .7-.2 1z"/></svg>
    <span>Call Us : +49 000 555 120-0</span>
  </div>
  <span class="sep"></span>
  <div class="item">
    <svg width="14" height="11" viewBox="0 0 24 18"><rect x="1" y="1" width="22" height="16" fill="none" stroke="#fff" stroke-width="2"/><path d="M1 1l11 9 11-9" fill="none" stroke="#fff" stroke-width="2"/></svg>
    <span>Email Now : info@lumenfix.example</span>
  </div>
  <span class="sep"></span>
  <div class="search"><span>Search Here......</span>
    <svg width="11" height="11" viewBox="0 0 24 24"><circle cx="14" cy="10" r="7" fill="none" stroke="#fff" stroke-width="2.5"/><path d="M9 15l-6 6" stroke="#fff" stroke-width="2.5"/></svg>
  </div>
</div>
<nav class="abs nav">
  <a href="https://lumenfix.example/en/lumenfix-english/">Home</a>
  <a href="#">Endoscope Repair</a>
  <a href="https://lumenfix.example/en/used-endoscopes/">Used Endoscopes</a>
  <a href="#">Endoscopy Systems</a>
  <a href="#">Endoscopy Accessories</a>
  <a href="https://lumenfix.example/en/purchase/">Purchase</a>
</nav>

<!-- hero -->
<section class="abs hero" role="img" aria-label="Blue-toned close-up of a flexible endoscope"></section>
<svg class="abs" style="left:0;top:720px" width="1200" height="82" viewBox="0 0 1200 82">
  <polygon points="0,13 1200,50 1200,82 0,82" fill="#7fb3e6"/>
  <polygon points="0,82 1200,40 1200,82" fill="#fff"/>
</svg>
<h1 class="abs hero-title">PUT YOUR ENDOSCOPE IN RELIABLE HANDS!</h1>
<p class="abs hero-text">LumenFix GmbH is specialised in the repair and sale of Aurelis, Pentrix and Kaminon flexible medical endoscopes. As a service-oriented company, we are at your side with our knowledge and skills!</p>
<a class="abs btn hero-btn btn-white" style="left:382px" href="#">Pick-up order</a>
<a class="abs btn hero-btn btn-dark" style="left:611px" href="#">Contact now</a>
<div class="abs arrow-circle" style="left:41px;top:413px"><svg width="10" height="12" viewBox="0 0 10 12"><path d="M7 1L2 6l5 5" fill="none" stroke="#fff" stroke-width="2"/></svg></div>
<div class="abs arrow-circle" style="left:1132px;top:413px"><svg width="10" height="12" viewBox="0 0 10 12"><path d="M3 1l5 5-5 5" fill="none" stroke="#fff" stroke-width="2"/></svg></div>
<div class="abs dots"><span></span><span></span><span></span></div>

<!-- about -->
<h2 class="abs h2" style="left:94px;top:914px">About us</h2>
<div class="abs copy" style="left:94px;top:966px;width:475px">
  <p>LumenFix GmbH is specialized in repairing and saling flexible endoscopes along with accessories and consumables. We offer endoscopes, processors, light sources, accessories and much more – with a focus on the manufacturers Aurelis, Pentrix and Kaminon.</p>
  <p style="margin-top:22px">We applied for foundation in 2020, whereby LumenFix emerged from another company in the same business field. For this reason, all employees have many years of experience. LumenFix is a reliable contact for doctors and hospitals.</p>
</div>
<a class="abs btn btn-blue" style="left:94px;top:1195px;width:135px;height:43px;font-size:16px;text-transform:uppercase" href="https://lumenfix.example/en/lumenfix-english">Read more</a>
<div class="abs about-accent"></div>
<div class="abs about-photo" role="img" aria-label="Clinician handling an endoscope beside an endoscopy tower"></div>

<!-- services -->
<h2 class="abs h2 center" style="top:1366px">Your future - our service</h2>
<p class="abs sub center" style="top:1413px">Endoscope repairs and second hand endoscopes from LumenFix – cause the outcome matters!</p>
<div class="abs svc-card"></div>
<div class="abs svc" style="left:84px;top:1487px">
  <div class="icon-circle"><svg width="52" height="52" viewBox="0 0 52 52"><path d="M10 42l20-20M34 8a9 9 0 0 0-6 12l-4 4 4 4 4-4a9 9 0 0 0 12-6l-5 2-4-4 2-5z" fill="none" stroke="#0a3f8f" stroke-width="4" stroke-linecap="round"/><path d="M8 10l6-2 16 16-4 4L10 12zM30 32l10 10" fill="none" stroke="#0a3f8f" stroke-width="4" stroke-linecap="round"/></svg></div>
  <h3>Repair</h3><h4>Endoscope repair service</h4>
  <p>Manufacturer-independent we repair and maintain endoscopes, individual components</p>
  <a class="btn" href="#">Repair request</a>
</div>
<div class="abs svc" style="left:426px;top:1520px">
  <div class="icon-circle"><svg width="52" height="52" viewBox="0 0 52 52"><circle cx="18" cy="34" r="10" fill="#0a3f8f"/><text x="18" y="39" text-anchor="middle" font-size="13" fill="#fff" font-family="Roboto">$</text><ellipse cx="36" cy="40" rx="9" ry="4" fill="none" stroke="#0a3f8f" stroke-width="3"/><path d="M30 24l6-10 6 10h-3v10h-6V24zM14 20l4-7 4 7" fill="#0a3f8f"/></svg></div>
  <h3>Sale</h3><h4>Used endoscopes</h4>
  <p>Our regular stock includes refurbished gastroscopes, coloscopes, bronchoscopes, cystoscopes and</p>
  <a class="btn" href="#">Purchase request</a>
</div>
<div class="abs svc" style="left:767px;top:1487px">
  <div class="icon-circle"><svg width="52" height="52" viewBox="0 0 52 52"><path d="M6 10h7l5 22h22l4-16H16" fill="none" stroke="#0a3f8f" stroke-width="4" stroke-linejoin="round"/><path d="M16 16h28l-4 16H18z" fill="#0a3f8f"/><circle cx="20" cy="40" r="4" fill="#0a3f8f"/><circle cx="38" cy="40" r="4" fill="#0a3f8f"/></svg></div>
  <h3>Purchase</h3><h4>Used endoscopes</h4>
  <p>We are very interested in buying your old endoscopes – even defective and dismantled!</p>
  <a class="btn" href="https://lumenfix.example/en/purchase/">Sell device</a>
</div>

<!-- outcome -->
<svg class="abs" style="left:0;top:1890px" width="1200" height="652" viewBox="0 0 1200 652">
  <defs>
    <linearGradient id="sideBlue" x1="0" y1="0" x2="1" y2="1"><stop offset="0" stop-color="#0a5cc2"/><stop offset="1" stop-color="#03378c"/></linearGradient>
  </defs>
  <polygon points="0,0 340,270 340,440 0,652" fill="url(#sideBlue)"/>
  <polygon points="1200,35 860,270 860,460 1045,560 1200,652" fill="url(#sideBlue)"/>
</svg>
<h2 class="abs h2 center" style="top:1955px">Cause the outcome matters!</h2>
<p class="abs sub center" style="top:2003px">Our service includes the manufacturers Aurelis, Pentrix and Kaminon!</p>

<div class="abs feat" style="left:66px;top:2077px"><span class="pin"></span>
  <div class="ic"><svg width="50" height="50" viewBox="0 0 50 50"><path d="M14 8v12a8 8 0 0 0 16 0V8M22 28v8a8 8 0 0 0 16 0v-6" fill="none" stroke="#fff" stroke-width="3"/><circle cx="38" cy="26" r="4" fill="none" stroke="#fff" stroke-width="3"/></svg></div>
  <h3>One company for everyone</h3><p>We are a service provider for doctors and hospitals!</p></div>
<div class="abs feat" style="left:338px;top:2130px"><span class="pin"></span>
  <div class="ic"><svg width="50" height="50" viewBox="0 0 50 50"><circle cx="25" cy="24" r="7" fill="#fff"/><path d="M12 42a13 13 0 0 1 26 0z" fill="#fff"/><circle cx="11" cy="18" r="3" fill="#fff"/><circle cx="39" cy="18" r="3" fill="#fff"/><circle cx="25" cy="9" r="3" fill="#fff"/></svg></div>
  <h3>Experience characterises us</h3><p>Our team has many years of experience in the business field!</p></div>
<div class="abs feat" style="left:610px;top:2077px"><span class="pin"></span>
  <div class="ic"><svg width="50" height="50" viewBox="0 0 50 50"><rect x="10" y="14" width="22" height="22" rx="6" fill="none" stroke="#fff" stroke-width="3"/><path d="M21 19v12M15 25h12M32 20c6 2 8 10 2 16" fill="none" stroke="#fff" stroke-width="3"/></svg></div>
  <h3>The product is close to our hearts</h3><p>We repair and sell second hand, flexible endoscopes!</p></div>
<div class="abs feat" style="left:882px;top:2130px"><span class="pin"></span>
  <div class="ic"><svg width="50" height="50" viewBox="0 0 50 50"><circle cx="21" cy="28" r="10" fill="none" stroke="#fff" stroke-width="4" stroke-dasharray="4 3"/><circle cx="21" cy="28" r="4" fill="#fff"/><circle cx="35" cy="15" r="6" fill="none" stroke="#fff" stroke-width="3" stroke-dasharray="3 2"/></svg></div>
  <h3>Services for everyone</h3><p>Our service includes the manufacturers Aurelis, Pentrix and Kaminon!</p></div>

<!-- used endoscopes -->
<h2 class="abs h2" style="left:92px;top:2586px">Used endoscopes</h2>
<p class="abs copy" style="left:92px;top:2635px;width:350px;line-height:23px">It is a long established fact that a reader will be distracted by the readable content of a page when looking at its layout. The point of using Lorem Ipsum is that it has a more-or-less normal distribution of letters, as opposed to using 'Content here, content here', making it look like readable English. Many desktop publishing packages and web page editors now use Lorem Ipsum as their default model text</p>
<div class="abs small-arrow" style="left:93px;top:2880px"><svg width="8" height="10" viewBox="0 0 8 10"><path d="M6 1L2 5l4 4" fill="none" stroke="#888" stroke-width="1.5"/></svg></div>
<div class="abs small-arrow" style="left:129px;top:2880px"><svg width="8" height="10" viewBox="0 0 8 10"><path d="M2 1l4 4-4 4" fill="none" stroke="#888" stroke-width="1.5"/></svg></div>

<article class="abs prod" style="left:489px;top:2568px">
  <div class="ph" role="img" aria-label="Surgeons in blue scrubs performing an endoscopy" style="background:linear-gradient(135deg,#9fd4e8,#3c8fc0 50%,#1d5d8f)"></div>
  <h3>Second hand Aurelis-endoscopes and -processors</h3>
  <p>LumenFix GmbH offers you excellent second hand Aurelis equipment (endoscopes and processors)</p>
  <a class="more" href="https://lumenfix.example/en/used-endoscopes/">Read More</a>
</article>
<article class="abs prod" style="left:812px;top:2568px">
  <div class="ph" role="img" aria-label="Endoscopy monitor and equipment in a lab" style="background:linear-gradient(135deg,#4a4f57,#1f2227 50%,#8a6b4a)"></div>
  <h3>Second hand Pentrix-endoscopes and -processors</h3>
  <p>Our second hand Pentrix equipment (endoscopes and processors) is an high-quality and cost-effective</p>
  <a class="more" href="https://lumenfix.example/en/used-endoscopes/">Read More</a>
</article>

<!-- cta & footer -->
<div class="abs footer-bg"></div>
<div class="abs cta">
  <h2>Join now, for get &nbsp;more details on<br>our services</h2>
  <a class="btn" href="#">Get in touch</a>
</div>

<div class="abs brand" style="top:3290px;left:102px;color:var(--white);font-size:17px"><span class="dot" style="width:12px;height:12px"></span>LumenFix</div>
<p class="abs f-text" style="left:94px;top:3352px;width:290px">LumenFix GmbH is specialised in the repair and sale of Aurelis, Pentrix and Kaminon flexible medical endoscopes.</p>

<h3 class="abs f-head" style="left:432px;top:3270px">Quick links</h3>
<ul class="abs f-links" style="left:432px;top:3303px">
  <li>Home</li><li>About Us</li><li>Purchase</li><li>Pick-Up Order</li><li>Contact Us</li>
</ul>
<h3 class="abs f-head" style="left:646px;top:3270px">Information links</h3>
<ul class="abs f-links" style="left:646px;top:3303px">
  <li>Endoscope Repair</li><li>Used Endoscopes</li><li>Endoscopy Systems</li><li>Endoscopy Accessories</li><li>Terms &amp; Conditions</li>
</ul>
<h3 class="abs f-head" style="left:881px;top:3270px">Stay connected</h3>
<div class="abs subscribe">Email Address<span class="send">SEND NOW</span></div>
<div class="abs f-text" style="left:881px;top:3362px;display:flex;align-items:center;gap:10px;font-weight:600">
  <svg width="15" height="11" viewBox="0 0 24 18"><rect x="1" y="1" width="22" height="16" fill="none" stroke="#fff" stroke-width="2"/><path d="M1 1l11 9 11-9" fill="none" stroke="#fff" stroke-width="2"/></svg>
  info@lumenfix.example
</div>
<div class="abs" style="left:1108px;top:3425px;width:38px;height:38px;border:3px solid var(--blue);border-radius:50%;display:flex;align-items:center;justify-content:center">
  <svg width="16" height="14" viewBox="0 0 16 14"><path d="M2 7l6-5 6 5M2 12l6-5 6 5" fill="none" stroke="#0a5cc2" stroke-width="2.2"/></svg>
</div>
<p class="abs f-text center" style="top:3464px">Copyright © 2022 LumenFix GmbH</p>

</body>
</html>
```